Harbinger and Lantern Website

We are a private investigation that people turn to when they seek answers. We provide all types of investigation services as well as security and debt collection but mainly we specialise in digital forensic investigation. This site will be the first representation that potential clients see. We need a site that can work on all browsers so not too many animations. The theme we are going for is "Pallor" the TV show but keeping the law enforcement look. We want it to expand on the logo of our company that is strength and pride (refer to files attached). The logo and mission statement must stand out.
The relevant info is attached in .doc documents
Updates

Hi,

I have uploaded a slightly different version of the logo and I do prefer the new version and made a FEW but important updates and additions to the website info. Sorry for the inconvenience.

Hi, 

Sorry just one last thing can you please put the following on the website 'Harbinger and Lantern is a South Australian owned business and we service all of Australia.' 

I have increased the budget.

Hi,

I've increased the budget slightly. I will continue to increase it as long as the quality of designs match it.

I have increased the budget. I will increase it more if I see some designs that warrant the increase.

I have extended the deadline by 3 days.

Hi,

Forget the brief and please take a look at this link and that is the type of design I want. I want people to look at it and think modern, professional, digital, forensic investigation. I have not seen anything that makes me think "wow" so please submit some new designs. I will increase the budget when I start to see designs that I like. 

regarding the last message, this is the link

https://www.vantorel-example.org

Reason: Have not seen anything that stands out from the rest.

Reason: To let designers finish off their current concepts that they may be working on.

Target Market(s)

Average to corporate people seeking professionalism and a firm that can supply answers that traditional law enforcement agencies fail to provide

Industry/Entity Type

Security

Requirements
Must have
• A professional QRD, Southern Tablelands Constabulary website look mixed with a theme from the TV show "Pallor" and the ability to download the business cards (refer to attached files)
Should not have
• cartoon images and anything relating to Ambrose Pettigrew

```html
<!DOCTYPE html>
<html lang="en">
<head>
<meta charset="utf-8">
<title>Harbinger and Lantern</title>
<link href="https://fonts.googleapis.com/css2?family=Arimo:wght@400;700&family=Oswald:wght@400;500&display=swap" rel="stylesheet">
<style>
:root{
  --gold-light:#f3dc93;
  --gold:#d5b256;
  --gold-dark:#9c7a2c;
  --gold-text:#e8b43a;
  --ink:#2b2414;
  --space-deep:#0a1422;
  --space-mid:#1d3550;
  --page:#1b1b1b;
  --panel:#262626;
  --card:#2f2f2f;
  --white:#ffffff;
  --muted:#c9c9c9;
  --footer-text:#bdbdbd;
}
*{margin:0;padding:0;box-sizing:border-box}
html,body{width:1092px;height:1200px;overflow:hidden;background:var(--page)}
body{position:relative;font-family:Arimo,Arial,sans-serif;color:var(--white)}

.topbar{position:absolute;left:0;top:0;width:1092px;height:53px;
  background:linear-gradient(#f6e6a9,var(--gold) 60%,#c7a148);border-bottom:1px solid #7a5d1e}
.brand{position:absolute;left:136px;top:8px;width:38px;height:38px;border-radius:50%;
  background:var(--ink);border:2px solid var(--gold-dark)}
.menu{position:absolute;left:180px;top:0;display:flex;height:53px}
.menu a{font-family:Oswald,sans-serif;font-size:15px;color:var(--ink);text-decoration:none;
  padding:0 18px;line-height:53px;border-left:1px solid rgba(120,90,30,.45)}
.menu a:last-child{border-right:1px solid rgba(120,90,30,.45)}
.call{position:absolute;left:782px;top:0;line-height:53px;font-family:Oswald,sans-serif;
  font-size:19px;color:var(--ink);display:flex;align-items:center;gap:8px}
.call .label{color:#8a6a25}

.hero{position:absolute;left:0;top:53px;width:1092px;height:493px;
  background:radial-gradient(ellipse at 62% 20%,#5a7a98 0%,var(--space-mid) 30%,var(--space-deep) 75%)}
.hero-emblem{position:absolute;left:136px;top:132px;width:250px;height:250px;border-radius:50%;
  background:var(--ink);border:6px solid var(--gold);display:flex;align-items:center;justify-content:center}
.hero-emblem span{font-family:Arimo,sans-serif;font-weight:700;font-size:22px;color:var(--gold-light);text-align:center;line-height:1.25}
.hero-title{position:absolute;left:453px;top:88px;width:560px;font-size:39px;line-height:44px;font-weight:400}
.hero-title strong{display:block;font-size:44px;letter-spacing:-1px}
.hero-rule{position:absolute;left:453px;top:282px;width:420px;height:1px;background:rgba(255,255,255,.3)}
.hero-copy{position:absolute;left:457px;top:297px;width:480px;font-size:13.5px;line-height:17.5px;color:#d7dde4}
.hero-pie{position:absolute;left:457px;top:398px;font-size:13.5px;color:#d7dde4}
.pillars{position:absolute;left:457px;top:439px;display:flex}
.pillar{display:flex;align-items:center;gap:9px;font-size:16px;margin-right:58px}
.pillar i{font-style:normal;width:28px;height:28px;border-radius:50%;background:var(--gold);
  color:var(--ink);font-size:13px;display:flex;align-items:center;justify-content:center}
.space-scene{position:absolute;inset:0}

.divider{position:absolute;left:0;top:546px;width:1092px;height:20px;background:linear-gradient(#5a5a5a,#2a2a2a)}

.services{position:absolute;left:0;top:566px;width:1092px;height:434px;
  background:radial-gradient(ellipse at 75% 30%,#3a3a3a 0%,#1e1e1e 60%)}
.services-head{position:absolute;left:112px;top:57px;width:860px;height:54px;background:var(--panel)}
.services-head .flag{position:absolute;left:0;top:0;width:24px;height:54px;background:#111}
.services-head h2{position:absolute;left:38px;top:-6px;font-family:Oswald,sans-serif;font-weight:400;
  font-size:56px;color:var(--gold-text);background:#1e1e1e;padding:0 14px}
.btn-all{position:absolute;left:802px;top:66px;width:166px;height:36px;
  background:linear-gradient(var(--gold-light),var(--gold-dark));color:var(--ink);font-family:Oswald,sans-serif;
  font-size:15px;display:flex;align-items:center;justify-content:center;border:1px solid #6d541c}
.card{position:absolute;top:125px;height:277px;background:var(--card);border:1px solid #444}
.card .photo{position:absolute;left:6px;top:7px;right:6px;height:112px}
.card h3{position:absolute;left:11px;top:130px;font-size:17px;font-weight:700}
.card p{position:absolute;left:11px;top:155px;right:10px;font-size:11px;line-height:14px;color:var(--muted)}
.card .more{position:absolute;left:13px;top:228px;width:106px;height:28px;
  background:linear-gradient(var(--gold-light),var(--gold-dark));color:var(--ink);font-size:13px;font-weight:700;
  display:flex;align-items:center;justify-content:center;gap:6px}

.footer{position:absolute;left:0;top:1000px;width:1092px;height:200px;background:#1a1a1a;border-top:1px solid #2e2e2e}
.footer h4{font-family:Oswald,sans-serif;font-weight:400;font-size:14px;color:var(--gold-text);margin-bottom:10px}
.footer .col{position:absolute;top:26px;font-size:11px;line-height:15.5px;color:var(--footer-text)}
.social{display:flex;gap:20px;align-items:center}
.social span{display:flex;align-items:center;gap:6px;font-size:10px}
.social b{width:22px;height:22px;background:#555;border-radius:2px;display:block}
.seal{position:absolute;left:880px;top:22px;width:76px;height:76px;border-radius:50%;
  background:radial-gradient(#3b3b3b,#222);border:2px solid #555}
</style>
</head>
<body>

<header class="topbar">
  <div class="brand" aria-hidden="true"></div>
  <nav class="menu">
    <a href="#">HOME</a><a href="#">WHO WE ARE</a><a href="#">SERVICES</a><a href="#">FAQ</a><a href="#">ENQUIRY</a><a href="#">CONTACT US</a>
  </nav>
  <div class="call">
    <svg width="20" height="20" viewBox="0 0 20 20" aria-hidden="true"><circle cx="10" cy="10" r="9" fill="none" stroke="#8a6a25" stroke-width="1.5"/><path d="M7 5l2 3-1 1.3c.6 1.3 1.5 2.2 2.7 2.7L12 11l3 2-1 2c-4 0-8-4-8-8z" fill="#8a6a25"/></svg>
    <span><span class="label">Call:</span> 0491 570 118</span>
  </div>
</header>

<section class="hero">
  <div class="space-scene" role="img" aria-label="Deep space backdrop with a faint handprint, Earth's horizon and an orbiting space station"></div>
  <div class="hero-emblem"><span>Harbinger<br>and Lantern</span></div>
  <h1 class="hero-title"><strong>Harbinger and Lantern</strong>is a South Australian Owned Business and We Service all of Australia</h1>
  <div class="hero-rule"></div>
  <p class="hero-copy">Through integrity and professionalism we will use our experience and resources as well as thinking outside the box to deliver results and services that exceed our clients' expectations. The team at Harbinger and Lantern are welcoming, understanding and are more than happy to meet all your needs, wants and expectations.</p>
  <p class="hero-pie">We employ the <b>P.I.E.</b> theory developed by our chief investigator.</p>
  <div class="pillars">
    <div class="pillar"><i>1</i>Professionalism</div>
    <div class="pillar"><i>2</i>Integrity</div>
    <div class="pillar"><i>3</i>Efficiency</div>
  </div>
</section>

<div class="divider"></div>

<section class="services">
  <div class="services-head"><div class="flag"></div><h2>SERVICES</h2></div>
  <a class="btn-all">VIEW ALL SERVICES</a>

  <article class="card" style="left:112px;width:212px">
    <div class="photo" role="img" aria-label="Photo of yellow unsolved case tape over case files" style="background:linear-gradient(135deg,#8c7a5a,#d8c04a 50%,#6e5e44)"></div>
    <h3>Unsolved Cases</h3>
    <p>If you are unsatisfied with the investigation performed by other private investigation agencies and or law enforcement we will.</p>
    <a class="more">Read More ›</a>
  </article>

  <article class="card" style="left:334px;width:207px">
    <div class="photo" role="img" aria-label="Photo of a group of young people in a confrontation" style="background:linear-gradient(135deg,#3c4f73,#8a92a8 50%,#2a3350)"></div>
    <h3>Bullying/Stalking</h3>
    <p>Is someone stalking you or bullying you? Well we will get the proof and evidence whether it be online and or in real life.</p>
    <a class="more">Read More ›</a>
  </article>

  <article class="card" style="left:550px;width:211px">
    <div class="photo" role="img" aria-label="Photo of a worried parent near a child's tricycle" style="background:linear-gradient(135deg,#6e6a66,#b9a79a 50%,#5a524c)"></div>
    <h3>Child Recovery</h3>
    <p>Our wide range of resources, skills and experience will help you find your children and get them back to you safe and sound.</p>
    <a class="more">Read More ›</a>
  </article>

  <article class="card" style="left:768px;width:212px">
    <div class="photo" role="img" aria-label="Photo of a dog behind cage bars" style="background:linear-gradient(135deg,#1a1a1a,#5a4a38 55%,#222)"></div>
    <h3>Animal Cruelty</h3>
    <p>Animals have feelings too and they deserve to live a happy and safe life. We can help to make sure that happens. If you suspect a...</p>
    <a class="more">Read More ›</a>
  </article>
</section>

<footer class="footer">
  <div class="col" style="left:109px">
    <h4>SITEMAP</h4>
    Home<br>About us<br>Faq's<br>Services<br>Contact Us
  </div>
  <div class="col" style="left:292px">
    <h4>CONTACT DETAILS</h4>
    Phone: 0491 570 118<br>managers@harbingerandlantern.example<br>Contact hours: 24 hours a day
  </div>
  <div class="col" style="left:557px">
    <h4>FOLLOW US</h4>
    <div class="social">
      <span><b></b>Chatterbook</span>
      <span><b></b>Chirper</span>
      <span><b></b>Linkwell</span>
    </div>
  </div>
  <div class="seal" aria-hidden="true"></div>
</footer>

</body>
</html>
```